Business Card Design Project

We would need a business name card for our online website business, http://www.plimo.com.sg/. We would need to include our website on the name card as well.

Target Market(s)

Adults and kids in Singapore, mainly expatriates

Industry/Entity Type

Business

Font styles to use
Sans Serif

Colors

Designer to choose colors to be used in the design.

Requirements
Must have
• Must include our "plimo" logo and we would like our name card to be printed on light craft paper material

```html
<!DOCTYPE html>
<html lang="en">
<head>
<meta charset="utf-8">
<title>plimo — business cards</title>
<link rel="stylesheet" href="https://fonts.googleapis.com/css2?family=Open+Sans:wght@400;700;800&display=swap">
<style>
  :root {
    --backdrop: #e9e7e3;
    --card-yellow: #f4ee8e;
    --card-yellow-deep: #ece35a;
    --ink: #15151a;
    --ring-orange: #f0a43a;
    --ring-text: #fff6e0;
    --navy: #3f4a94;
    --white: #ffffff;
    --band-cyan: #2a9fd6;
    --band-magenta: #e31f9c;
    --band-yellow: #f6ea2a;
    --band-navy: #2b2f7a;
  }
  * { box-sizing: border-box; margin: 0; padding: 0; }
  html, body {
    width: 1200px; height: 800px; overflow: hidden;
    background: var(--backdrop);
    font-family: "Open Sans", Arial, sans-serif;
  }
  .canvas { position: relative; width: 1200px; height: 800px; }

  .card-front {
    position: absolute; left: 140px; top: 130px;
    width: 330px; height: 540px;
    background: var(--card-yellow);
    box-shadow: 0 6px 18px rgba(0,0,0,.18);
    display: flex;
  }
  .edge-bands {
    width: 16px; height: 100%;
    display: grid; grid-template-rows: repeat(12, 1fr);
  }
  .edge-bands span:nth-child(4n+1) { background: var(--band-cyan); }
  .edge-bands span:nth-child(4n+2) { background: var(--band-magenta); }
  .edge-bands span:nth-child(4n+3) { background: var(--band-yellow); }
  .edge-bands span:nth-child(4n+4) { background: var(--band-navy); }
  .edge-bands--right span:nth-child(4n+1) { background: var(--band-navy); }
  .edge-bands--right span:nth-child(4n+2) { background: var(--band-yellow); }
  .edge-bands--right span:nth-child(4n+3) { background: var(--band-magenta); }
  .edge-bands--right span:nth-child(4n+4) { background: var(--band-cyan); }
  .front-body { flex: 1; position: relative; }
  .wordmark {
    position: absolute; left: 50%; top: 50%;
    transform: translate(-50%, -50%) rotate(90deg);
    font-weight: 800; font-size: 120px; letter-spacing: 2px;
    color: var(--ink); line-height: 1; white-space: nowrap;
  }

  .card-back {
    position: absolute; left: 540px; top: 230px;
    width: 560px; height: 340px;
    background: linear-gradient(135deg, var(--card-yellow) 0%, var(--card-yellow-deep) 100%);
    box-shadow: 0 6px 18px rgba(0,0,0,.18);
  }
  .card-back svg { display: block; }
  .ring-text { font-size: 13px; fill: var(--ring-text); font-weight: 400; letter-spacing: .5px; }
  .holder-name { font-size: 17px; font-weight: 700; fill: var(--ink); letter-spacing: 1.5px; }
  .badge-name { font-size: 34px; font-weight: 700; fill: var(--white); }
</style>
</head>
<body>
<main class="canvas">

  <section class="card-front" aria-label="Card front">
    <div class="edge-bands edge-bands--left">
      <span></span><span></span><span></span><span></span>
      <span></span><span></span><span></span><span></span>
      <span></span><span></span><span></span><span></span>
    </div>
    <div class="front-body">
      <div class="wordmark">PLIMO</div>
    </div>
    <div class="edge-bands edge-bands--right">
      <span></span><span></span><span></span><span></span>
      <span></span><span></span><span></span><span></span>
      <span></span><span></span><span></span><span></span>
    </div>
  </section>

  <section class="card-back" aria-label="Card back">
    <svg width="560" height="340" viewBox="0 0 560 340">
      <defs>
        <path id="arc-ring-top" d="M 149 170 A 131 131 0 0 1 411 170"/>
        <path id="arc-ring-bottom" d="M 139 170 A 141 141 0 0 0 421 170"/>
        <path id="arc-name-top" d="M 174 170 A 106 106 0 0 1 386 170"/>
        <path id="arc-name-bottom" d="M 160 170 A 120 120 0 0 0 400 170"/>
      </defs>
      <circle class="contact-ring" cx="280" cy="170" r="136" fill="none" stroke="var(--ring-orange)" stroke-width="26"/>
      <text class="ring-text"><textPath href="#arc-ring-top" startOffset="50%" text-anchor="middle">8 Harbour Lane #05-11 Singapore 038812</textPath></text>
      <text class="ring-text"><textPath href="#arc-ring-bottom" startOffset="50%" text-anchor="middle">www.plimo.com.sg | email@plimocorp.com | 6100 2345</textPath></text>
      <text class="holder-name"><textPath href="#arc-name-top" startOffset="50%" text-anchor="middle">MEI TAN</textPath></text>
      <text class="holder-name"><textPath href="#arc-name-bottom" startOffset="50%" text-anchor="middle">MEI TAN</textPath></text>
      <circle class="badge" cx="280" cy="170" r="82" fill="var(--navy)"/>
      <text class="badge-name" x="280" y="182" text-anchor="middle">plimo</text>
    </svg>
  </section>

</main>
</body>
</html>
```